Need Business Card Design, Letterhead and a Basic Form layout based on Existing Logo

We need (1) a business card design, (2) a letterhead design and (3) a basic form layout for an international holding company. This holding company has just formed two (2) sub-companies. The logo is the same for each company with only a simple word change for each company. The business card, letterhead and form design will be essentially the same for each company... with only the one word change being different.
The names of the companies are as follows:
1. Ridgeway Trust Services
2. Ridgeway Immigration Services
The design for the business card, letterhead and Form must be strong, clean and classy.
Our clients will be older, wealthy and mostly Asian. The design must project strength, stability and confidence.
The card may contain the following data:
1. The Logo
2. The name of the person
3. The title of the person
4. The address of the company
5. The Company Phone number
6. The personal mobile number
7. The Skype number (VOIP)
8. The WICKR number (IM)
9. The email
10. The website
We will attach AI files of our logo for the "Ridgeway Trust Services" company in the colors Black/White and Blue in both Horizontal and Vertical format... We have also included separate files of the logo icon.
We uploaded the AI files to give the designer the maximum options regarding color and effects. We included the separate files for the icon because we would like to give the designer the option of a watermark. Also, we think it might be nice to highlight the icon on the back of the card perhaps with the website address.
We are not sure which colors or color combinations would be best for these two companies. We know the colors must again project strength, stability and confidence. Perhaps, a combination that might include Tan, Black and White... not sure... need design help... remember this has to have the presence of a bank-like institution... no cartoonish designs or flashy color combinations... please.
The basic form layout will be used for various questionaires, input sheets and instructions.... etc.
NOTE: The fonts used in the logo are Trajan Pro Bold for word "RIDGEWAY" and Trajan Pro Regular for "XXXXXXXXX SERVICES".

```html
<!DOCTYPE html>
<html lang="en">
<head>
<meta charset="utf-8">
<title>Ridgeway Trust Services – Business Card</title>
<link href="https://fonts.googleapis.com/css2?family=Cinzel:wght@400;600&family=Open+Sans:wght@400&display=swap" rel="stylesheet">
<style>
  :root {
    --backdrop: #e9e6e1;
    --card: #ffffff;
    --ink: #1c1c1c;
    --band: #1e1e1e;
    --stripe: #9a9a9a;
    --stripe-light: #c9c9c9;
    --muted: #3a3a3a;
    --rule: #b5b5b5;
    --on-band: #ffffff;
    --on-band-soft: #dcdcdc;
  }
  * { box-sizing: border-box; margin: 0; padding: 0; }
  html, body { width: 1200px; height: 720px; overflow: hidden; background: var(--backdrop); }
  .canvas {
    position: relative; width: 1200px; height: 720px;
    display: flex; align-items: center; justify-content: center; gap: 40px;
  }
  .card {
    position: relative; width: 540px; height: 309px;
    background: var(--card); overflow: hidden;
    box-shadow: 0 2px 10px rgba(0,0,0,0.15);
  }

  /* Wordmark */
  .wordmark { position: absolute; display: flex; align-items: center; color: var(--ink); font-family: "Cinzel", serif; font-weight: 600; z-index: 2; }
  .wordmark-square { background: var(--ink); flex: none; }
  .wordmark-name { display: flex; flex-direction: column; line-height: 1; }

  .card-front .wordmark { left: 100px; top: 24px; gap: 22px; }
  .card-front .wordmark-square { width: 48px; height: 48px; }
  .card-front .wordmark-primary { font-size: 30px; letter-spacing: 1px; }
  .card-front .wordmark-secondary { font-size: 15px; margin-top: 3px; padding-left: 2px; }

  /* Contacts */
  .contacts {
    position: absolute; top: 94px; left: 0; width: 100%; z-index: 2;
    font-family: "Open Sans", sans-serif; font-size: 11.5px; color: var(--muted); line-height: 1.45;
  }
  .contacts-office { position: absolute; right: 296px; text-align: right; }
  .contacts-online { position: absolute; left: 262px; }
  .contacts-divider { position: absolute; left: 253px; top: 2px; width: 1px; height: 64px; background: var(--rule); }
  .contact-line { display: flex; align-items: center; gap: 5px; white-space: nowrap; }
  .contacts-office .contact-line { justify-content: flex-end; }
  .contact-icon { width: 10px; height: 10px; flex: none; }

  /* Name band */
  .band { position: absolute; inset: 0; width: 100%; height: 100%; z-index: 1; }
  .holder { position: absolute; left: 34px; top: 246px; color: var(--on-band); font-family: "Cinzel", serif; line-height: 1.15; z-index: 2; }
  .holder-name { font-size: 17px; font-weight: 600; letter-spacing: 0.5px; }
  .holder-title { font-size: 11px; font-weight: 400; letter-spacing: 0.5px; color: var(--on-band-soft); }

  /* Back */
  .card-back .wordmark { left: 50%; top: 56px; transform: translateX(-50%); flex-direction: column; gap: 26px; }
  .card-back .wordmark-square { width: 66px; height: 66px; }
  .card-back .wordmark-name { align-items: center; }
  .card-back .wordmark-primary { font-size: 38px; letter-spacing: 1.5px; }
  .card-back .wordmark-secondary { font-size: 18px; margin-top: 4px; }
  .website {
    position: absolute; left: 0; right: 0; top: 250px; text-align: center;
    font-family: "Open Sans", sans-serif; font-size: 15px; letter-spacing: 3px; color: var(--muted);
  }
</style>
</head>
<body>
<main class="canvas">

  <section class="card card-front" aria-label="Business card front">
    <div class="wordmark">
      <span class="wordmark-square"></span>
      <span class="wordmark-name">
        <span class="wordmark-primary">RIDGEWAY</span>
        <span class="wordmark-secondary">Trust Services</span>
      </span>
    </div>

    <div class="contacts">
      <div class="contacts-office">
        <p class="contact-line">
          <svg class="contact-icon" viewBox="0 0 10 10"><path d="M2 0.5 L3.6 2.6 L2.8 3.6 C3.4 5 4.8 6.5 6.3 7.2 L7.3 6.4 L9.5 8 L8.4 9.5 C4.5 9 1 5.5 0.5 1.6 Z" fill="#1c1c1c"/></svg>
          012-555-0147
        </p>
        <p class="contact-line">
          <svg class="contact-icon" viewBox="0 0 10 10"><rect x="2.5" y="0.5" width="5" height="9" rx="1" fill="#1c1c1c"/><rect x="3.4" y="1.6" width="3.2" height="5.6" fill="#fff"/></svg>
          012-555-0147
        </p>
        <p class="contact-line">Street Name, City Name</p>
        <p class="contact-line">Zip Code-00000</p>
      </div>
      <span class="contacts-divider"></span>
      <div class="contacts-online">
        <p class="contact-line">
          <svg class="contact-icon" viewBox="0 0 10 10"><circle cx="5" cy="5" r="4.5" fill="#4a4a4a"/></svg>
          012-555-0147
        </p>
        <p class="contact-line">
          <svg class="contact-icon" viewBox="0 0 10 10"><rect x="0.5" y="0.5" width="9" height="9" fill="#4a4a4a"/></svg>
          012-555-0147
        </p>
        <p class="contact-line">
          <svg class="contact-icon" viewBox="0 0 10 10"><rect x="0.5" y="2" width="9" height="6.5" fill="#1c1c1c"/><path d="M0.8 2.4 L5 5.6 L9.2 2.4" fill="none" stroke="#fff" stroke-width="0.9"/></svg>
          inquiry@ridgewaytrust.com
        </p>
        <p class="contact-line">
          <svg class="contact-icon" viewBox="0 0 10 10"><circle cx="5" cy="5" r="4.3" fill="none" stroke="#1c1c1c" stroke-width="1"/><ellipse cx="5" cy="5" rx="1.8" ry="4.3" fill="none" stroke="#1c1c1c" stroke-width="0.8"/><line x1="0.7" y1="5" x2="9.3" y2="5" stroke="#1c1c1c" stroke-width="0.8"/></svg>
          www.ridgewaytrust.com
        </p>
      </div>
    </div>

    <svg class="band" viewBox="0 0 540 309" preserveAspectRatio="none" aria-hidden="true">
      <path d="M0 214 C150 196 300 206 410 178 C470 162 505 138 540 126 L540 134 C505 146 472 170 412 186 C302 214 150 205 0 224 Z" fill="var(--stripe-light)"/>
      <path d="M0 224 C150 205 302 214 412 186 C472 170 505 146 540 134 L540 142 C506 154 474 178 414 194 C304 222 150 214 0 232 Z" fill="var(--stripe)"/>
      <path d="M0 232 C150 214 304 222 414 194 C474 178 506 154 540 142 L540 166 C470 178 410 215 330 248 C260 276 230 309 190 309 L0 309 Z" fill="var(--band)"/>
      <path d="M190 309 C230 309 260 276 330 248 C410 215 470 178 540 166 L540 174 C472 188 414 224 336 256 C270 284 244 309 212 309 Z" fill="var(--stripe)"/>
    </svg>

    <div class="holder">
      <p class="holder-name">YOUR NAME</p>
      <p class="holder-title">TITLE</p>
    </div>
  </section>

  <section class="card card-back" aria-label="Business card back">
    <div class="wordmark">
      <span class="wordmark-square"></span>
      <span class="wordmark-name">
        <span class="wordmark-primary">RIDGEWAY</span>
        <span class="wordmark-secondary">Trust Services</span>
      </span>
    </div>
    <p class="website">www.ridgewaytrust.com</p>
  </section>

</main>
</body>
</html>
```